Bully breed rescue website

I need a website for my bully breed rescue. We rescue bully breeds from up and down the east coast of the United States and train them as service dogs for people with limited mobility disabilities. I don't want a lot of white space. I want it to be modern and slick and colorful and still look professional. I want it to be different and have a lot of wow factor. I linked a copy of my logo.

Number of Pages Required

5+ page

Font styles to use
Sans Serif

Colors

Designer to choose colors to be used in the design.

Requirements
Must have
• Moving aspects. Blog and ecommerce.
• 1.) Home page
• 2.) Services- something modular
• 3.) About US
• 4.) Blog
• 5.) Application page
• 6.) Donation page
• 7.) Contact Us
Nice to have
• Large Slider of photos on home page
• vertical menu bar
Should not have
• Lots of white space. Dont want it to look like a template or any other site

```html
<!DOCTYPE html>
<html lang="en">
<head>
<meta charset="utf-8">
<title>Stand Up Pup – Bully Breed Rescue</title>
<link href="https://fonts.googleapis.com/css2?family=Bangers&family=Cinzel:wght@700&family=Lato:wght@400;700;900&display=swap" rel="stylesheet">
<style>
:root{
  --red:#e4222f;
  --red-dark:#b5121d;
  --yellow:#fdd21c;
  --yellow-dark:#e9b800;
  --ink:#1d1d1d;
  --grey:#f1f1f1;
  --muted:#6b6b6b;
  --white:#ffffff;
  --footer:#1a1616;
}
*{box-sizing:border-box;margin:0;padding:0}
html,body{width:1200px;height:3025px;overflow:hidden}
body{position:relative;font-family:"Lato",Arial,sans-serif;color:var(--ink);background:var(--white)}
.section{position:absolute;left:0;width:1200px}
.display{font-family:"Bangers","Impact",sans-serif;letter-spacing:1.5px}
.section-title{position:absolute;left:0;width:100%;text-align:center;font-size:42px;display:flex;justify-content:center;align-items:center;gap:14px}
.title-dot{width:34px;height:34px;border-radius:50%;border:3px solid var(--ink);background:var(--white)}
.btn{display:inline-block;border-radius:20px;font-weight:700;font-size:13px;text-transform:uppercase;letter-spacing:.5px}
.arrow{position:absolute;width:20px;height:40px}
.arrow svg{width:100%;height:100%}

/* header */
.topbar{top:0;height:66px;background:var(--white)}
.phone{position:absolute;left:176px;top:20px;display:flex;align-items:center;gap:10px;font-weight:700;font-size:15px}
.icon-round{width:24px;height:24px;border-radius:50%;background:var(--yellow);display:flex;align-items:center;justify-content:center;border:1px solid var(--ink)}
.socials{display:flex;gap:6px;margin-left:12px}
.social{width:22px;height:22px;border-radius:50%;background:var(--yellow);border:1px solid var(--ink)}
.donate-top{position:absolute;right:176px;top:16px;background:var(--yellow);border:2px solid var(--ink);padding:8px 30px 8px 56px;color:var(--ink);font-size:14px}
.navbar{top:66px;height:31px;background:var(--red)}
.nav{position:absolute;top:0;height:31px;display:flex;gap:36px;align-items:center;font-size:12px;color:var(--white);text-transform:uppercase;letter-spacing:.5px}
.nav.left{left:176px}.nav.right{left:736px}
.nav .active{color:var(--yellow)}
.brand{position:absolute;left:508px;top:12px;width:184px;height:150px;border-radius:50%;background:var(--white);display:flex;align-items:center;justify-content:center;z-index:3;box-shadow:0 3px 8px rgba(0,0,0,.25)}
.brand span{font-family:"Bangers","Impact",sans-serif;font-size:30px;color:var(--red-dark);letter-spacing:1px}

/* hero */
.hero{top:97px;height:508px;background:linear-gradient(100deg,#c9803a 0%,#e8a04c 35%,#f2b662 60%,#b87a3e 100%)}
.hero-photo{position:absolute;inset:0}
.hero-title{position:absolute;left:176px;top:188px;font-size:38px;color:var(--white);line-height:1.15;text-shadow:0 2px 4px rgba(0,0,0,.35)}
.hero-btn{position:absolute;left:176px;top:280px;background:var(--red);color:var(--white);padding:9px 20px 9px 50px;border:2px solid var(--ink)}
.dots{position:absolute;left:566px;top:462px;display:flex;gap:8px}
.dots i{width:8px;height:8px;border-radius:50%;background:rgba(255,255,255,.6)}
.dots i.on{background:var(--ink)}
.hero-side{position:absolute;top:210px;width:36px;height:64px;background:rgba(40,40,40,.7)}

/* about */
.about{top:605px;height:405px;background:linear-gradient(90deg,#ececec 0%,#fafafa 40%,#fff 100%)}
.about-lead{position:absolute;left:176px;top:106px;width:426px;font-size:13px;font-weight:700;text-transform:uppercase;line-height:1.9;letter-spacing:.6px}
.about-body{position:absolute;left:176px;top:186px;width:426px;font-size:11.5px;line-height:2.1;color:var(--muted)}
.read-more{position:absolute;left:176px;top:326px;background:var(--yellow);border:2px solid var(--ink);padding:7px 20px}
.about-photo{position:absolute;left:656px;top:114px;width:366px;height:246px;border-radius:60px 0 0 0;background:linear-gradient(135deg,#d9d9d9,#b4875a 55%,#8e6a43);border-bottom:5px solid var(--red);border-right:5px solid var(--yellow)}

/* services */
.services{top:1010px;height:430px;background:linear-gradient(180deg,#e4222f,#d51b28)}
.services .section-title{top:60px;color:var(--ink)}
.service{position:absolute;top:130px;width:204px;text-align:center}
.service .photo{width:204px;height:204px;border-radius:50%;border:4px solid var(--white);background:linear-gradient(135deg,#caa381,#8a6a4e)}
.service.on .photo{border-color:var(--yellow);background:linear-gradient(135deg,#5aa6a0,#c8b89a)}
.service .label{margin-top:18px;font-size:22px;color:var(--white)}
.service.on .label{color:var(--yellow)}

/* testimonial */
.testimonials{top:1440px;height:295px;background:var(--grey)}
.testimonials .section-title{top:38px}
.testimonial{position:absolute;top:114px;width:420px;height:120px}
.avatar{position:absolute;left:0;top:0;width:118px;height:118px;border-radius:50%;border:4px solid var(--red);background:linear-gradient(160deg,#d7c2ae,#8f7c6c)}
.quote{position:absolute;left:160px;top:16px;width:256px;font-size:10px;line-height:1.75;font-style:italic;color:var(--muted)}
.quote .more{color:var(--red);font-style:normal}
.client{position:absolute;left:138px;top:98px;font-size:11px;font-weight:900;color:var(--red)}
.stars{color:var(--yellow);margin-left:8px;letter-spacing:1px}

/* blog */
.blog{top:1735px;height:485px;background:var(--yellow)}
.blog .section-title{top:42px}
.post{position:absolute;top:120px;width:264px;height:310px;background:var(--white);box-shadow:0 4px 10px rgba(0,0,0,.2);text-align:center}
.post .photo{height:166px;background:linear-gradient(135deg,#b49276,#6e5a4a)}
.post .date{position:absolute;left:72px;top:154px;width:120px;height:24px;border-radius:12px;background:var(--yellow);font-size:11px;font-weight:700;line-height:24px}
.post h3{font-family:"Cinzel",Georgia,serif;font-size:13.5px;margin:30px 16px 12px;line-height:1.35}
.post p{font-size:11px;line-height:1.9;color:var(--muted);padding:0 26px}
.post .more{color:var(--red)}

/* adoptees */
.adoptees{top:2220px;height:300px;background:linear-gradient(90deg,#efefef,#fff 50%,#efefef)}
.adoptees .section-title{top:42px}
.adoptee{position:absolute;top:118px;width:200px;height:132px;border-radius:10px;background:linear-gradient(135deg,#7fa35b,#c9b08a)}
.adoptee.active{background:#4a4a4a;text-align:center;color:var(--white)}
.adoptee.active h4{font-weight:400;font-size:18px;margin-top:18px}
.adoptee.active p{font-size:10px;line-height:1.5;margin:4px 22px}
.adopt-btn{display:inline-block;margin-top:8px;border:1px solid var(--white);padding:5px 12px;font-size:12px;letter-spacing:.5px}

/* subscribe */
.subscribe{top:2520px;height:205px;background:var(--red)}
.mail-icon{position:absolute;left:210px;top:68px;width:50px;height:38px}
.subscribe h2{position:absolute;left:276px;top:66px;font-size:18px;color:var(--white);font-weight:900}
.subscribe .sub{position:absolute;left:276px;top:92px;font-size:11px;color:var(--white);font-weight:700}
.signup{position:absolute;left:210px;top:128px;display:flex}
.signup .field{width:254px;height:36px;background:var(--white);font-size:11px;color:#999;padding:11px 16px}
.signup .go{width:116px;height:36px;background:var(--yellow);font-size:12px;font-weight:900;text-align:center;line-height:36px}
.pups{position:absolute;left:632px;top:20px;width:300px;height:170px;border-radius:50% 50% 14px 14px;background:linear-gradient(160deg,#f3e2cf,#c48a5a)}

/* footer */
.footer{top:2725px;height:300px;background:var(--footer);color:var(--white)}
.footer h5{position:absolute;top:30px;font-family:"Cinzel",Georgia,serif;font-size:16px;font-weight:700;letter-spacing:1px}
.links{position:absolute;left:176px;top:80px;list-style:none;font-size:10px;line-height:23.5px;text-transform:uppercase}
.links li::before{content:"›";color:var(--red);margin-right:10px}
.contact{position:absolute;left:362px;top:80px;font-size:10.5px;line-height:1.6}
.contact .row{display:flex;gap:10px;margin-bottom:16px}
.contact .row b{font-size:13px}
.map{position:absolute;left:574px;top:86px;width:210px;height:148px;background:linear-gradient(135deg,#ebe6dc,#d6d0c4);border:2px solid var(--white)}
.foot-brand{position:absolute;left:846px;top:86px;width:120px;height:120px;border-radius:50%;border:2px solid var(--white);display:flex;align-items:center;justify-content:center}
.foot-brand span{font-family:"Bangers","Impact",sans-serif;font-size:22px;color:var(--white)}
.foot-socials{position:absolute;left:872px;top:214px;display:flex;gap:8px}
.copyright{position:absolute;left:0;bottom:10px;width:100%;text-align:center;font-size:9px;letter-spacing:.5px;border-top:1px solid #333;padding-top:10px}
</style>
</head>
<body>

<header class="section topbar">
  <div class="phone">
    <span class="icon-round"><svg width="12" height="12" viewBox="0 0 24 24"><path d="M6.6 10.8a15.1 15.1 0 0 0 6.6 6.6l2.2-2.2a1 1 0 0 1 1-.25 11.4 11.4 0 0 0 3.6.57 1 1 0 0 1 1 1V20a1 1 0 0 1-1 1A17 17 0 0 1 3 4a1 1 0 0 1 1-1h3.5a1 1 0 0 1 1 1c0 1.25.2 2.45.57 3.57a1 1 0 0 1-.25 1z" fill="#1d1d1d"/></svg></span>
    555-204-3187
    <span class="socials"><i class="social"></i><i class="social"></i><i class="social"></i></span>
  </div>
  <div class="btn donate-top">Donate Now</div>
</header>

<nav class="section navbar">
  <div class="nav left"><span class="active">Home</span><span>About Us</span><span>Services</span><span>Blog</span></div>
  <div class="nav right"><span>Application</span><span>Donation</span><span>Contact Us</span></div>
</nav>
<div class="brand"><span>Stand Up Pup</span></div>

<section class="section hero">
  <div class="hero-photo" role="img" aria-label="Bulldog lying in autumn grass at sunset"></div>
  <div class="hero-side" style="left:0"></div>
  <div class="hero-side" style="right:0"></div>
  <h1 class="hero-title display">Properly Trained, a Man<br>Can Be Bull's Best Friend</h1>
  <div class="btn hero-btn">Contact Us Now</div>
  <div class="dots"><i></i><i class="on"></i><i></i><i></i></div>
</section>

<section class="section about">
  <h2 class="section-title display" style="top:28px"><i class="title-dot"></i>About Us</h2>
  <p class="about-lead">We rescue bully breeds from up and down the east coast of the United States and train them as service dogs for people with limited mobility disabilities.</p>
  <p class="about-body">Lorem ipsum dolor sit amet, consectetur adipiscing elit. Aenean gravida sagittis ex gravida vehicula. Mauris consectetur, arcu sed ornare hendrerit, metus neque placerat tellus, in elementum ante ex vitae leo. Phasellus posuere consequat purus, sit amet egestas eros porttitor rutrum. Nam in sem sit amet quam sollicitudin sodales. Donec feugiat sed lacus eget laoreet.</p>
  <div class="btn read-more">Read More</div>
  <div class="about-photo" role="img" aria-label="Bulldog looking up at a trainer's pointing hand"></div>
</section>

<section class="section services">
  <h2 class="section-title display"><i class="title-dot"></i>Our Services</h2>
  <div class="arrow" style="left:124px;top:216px"><svg viewBox="0 0 20 40"><path d="M16 4 4 20l12 16" stroke="#7a0c14" stroke-width="3" fill="none"/></svg></div>
  <div class="service" style="left:176px"><div class="photo" role="img" aria-label="Relaxed bulldog lying down"></div><div class="label display">Rescue</div></div>
  <div class="service on" style="left:392px"><div class="photo" role="img" aria-label="Bulldog at a veterinary check-up"></div><div class="label display">Rehabilitate</div></div>
  <div class="service" style="left:604px"><div class="photo" role="img" aria-label="Bulldog playing with a ball on grass"></div><div class="label display">Training</div></div>
  <div class="service" style="left:818px"><div class="photo" role="img" aria-label="Family cuddling their adopted dog"></div><div class="label display">Adopt</div></div>
  <div class="arrow" style="left:1056px;top:216px"><svg viewBox="0 0 20 40"><path d="M4 4l12 16L4 36" stroke="#7a0c14" stroke-width="3" fill="none"/></svg></div>
</section>

<section class="section testimonials">
  <h2 class="section-title display"><i class="title-dot"></i>Client Testimonial</h2>
  <div class="arrow" style="left:124px;top:150px"><svg viewBox="0 0 20 40"><path d="M16 4 4 20l12 16" stroke="#c9c9c9" stroke-width="3" fill="none"/></svg></div>
  <div class="testimonial" style="left:176px">
    <div class="avatar" role="img" aria-label="Portrait of a smiling client"></div>
    <p class="quote">Our dog changed daily life at home. Training was patient and kind, and every visit felt like family. Highly recommended for anyone... <span class="more">[+]</span></p>
    <div class="client">DALE HARTWICK<span class="stars">★★★★★</span></div>
  </div>
  <div class="testimonial" style="left:616px">
    <div class="avatar" role="img" aria-label="Portrait of a smiling client"></div>
    <p class="quote">From the first call to adoption day the team guided us. Our new companion helps me move around with confidence every... <span class="more">[+]</span></p>
    <div class="client">NINA CALLOWAY<span class="stars">★★★★★</span></div>
  </div>
  <div class="arrow" style="left:1056px;top:150px"><svg viewBox="0 0 20 40"><path d="M4 4l12 16L4 36" stroke="#c9c9c9" stroke-width="3" fill="none"/></svg></div>
</section>

<section class="section blog">
  <h2 class="section-title display"><i class="title-dot"></i>Our Blog</h2>
  <div class="arrow" style="left:124px;top:256px"><svg viewBox="0 0 20 40"><path d="M16 4 4 20l12 16" stroke="#fff" stroke-width="3" fill="none"/></svg></div>
  <article class="post" style="left:176px"><div class="photo" role="img" aria-label="French bulldog puppy held in hands"></div><div class="date">23 April 2018</div><h3>Lorem ipsum dolor sitamet consectetur adipiscing elit.</h3><p>Lorem ipsum dolor sit amet, consectetur adipiscing elites. Aenean gravida sagittis ex gravida vehicula. Mauris consectetur... <span class="more">[+]</span></p></article>
  <article class="post" style="left:468px"><div class="photo" role="img" aria-label="Bulldog standing on a road"></div><div class="date">25 April 2018</div><h3>Lorem ipsum dolor sitamet consectetur adipiscing elit.</h3><p>Lorem ipsum dolor sit amet, consectetur adipiscing elites. Aenean gravida sagittis ex gravida vehicula. Mauris consectetur... <span class="more">[+]</span></p></article>
  <article class="post" style="left:760px"><div class="photo" role="img" aria-label="Two bulldogs tugging a stick on grass"></div><div class="date">18 May 2018</div><h3>Lorem ipsum dolor sitamet consectetur adipiscing elit.</h3><p>Lorem ipsum dolor sit amet, consectetur adipiscing elites. Aenean gravida sagittis ex gravida vehicula. Mauris consectetur... <span class="more">[+]</span></p></article>
  <div class="arrow" style="left:1056px;top:256px"><svg viewBox="0 0 20 40"><path d="M4 4l12 16L4 36" stroke="#fff" stroke-width="3" fill="none"/></svg></div>
</section>

<section class="section adoptees">
  <h2 class="section-title display"><i class="title-dot"></i>Adoptees</h2>
  <div class="arrow" style="left:124px;top:164px"><svg viewBox="0 0 20 40"><path d="M16 4 4 20l12 16" stroke="#c9c9c9" stroke-width="3" fill="none"/></svg></div>
  <div class="adoptee" style="left:176px" role="img" aria-label="Bulldog sitting on a lawn"></div>
  <div class="adoptee" style="left:392px;background:linear-gradient(135deg,#8a6048,#d8cfc4)" role="img" aria-label="White bulldog in front of a brick wall"></div>
  <div class="adoptee active" style="left:608px"><h4>Scarlett</h4><p>Lorem ipsum dolor sit amet, consectetur adipiscing elit.</p><span class="adopt-btn">ADOPT NOW</span></div>
  <div class="adoptee" style="left:824px" role="img" aria-label="French bulldog standing in a field"></div>
  <div class="arrow" style="left:1056px;top:164px"><svg viewBox="0 0 20 40"><path d="M4 4l12 16L4 36" stroke="#c9c9c9" stroke-width="3" fill="none"/></svg></div>
</section>

<section class="section subscribe">
  <svg class="mail-icon" viewBox="0 0 50 38"><rect x="1" y="1" width="48" height="36" fill="#fff"/><path d="M1 1l24 20L49 1" stroke="#e4222f" stroke-width="2" fill="none"/></svg>
  <h2>Let's Subscribe For Get In Touch</h2>
  <p class="sub">Lorem ipsum dolor sit amet, consectetur adipiscing elit gravida.</p>
  <div class="signup"><div class="field">Enter Your Email</div><div class="go">SUBSCRIBE</div></div>
  <div class="pups" role="img" aria-label="Litter of bulldog puppies"></div>
</section>

<footer class="section footer">
  <h5 style="left:176px">QUICK LINKS</h5>
  <h5 style="left:362px">CONTACT INFO</h5>
  <h5 style="left:574px">FIND US ON MAP</h5>
  <h5 style="left:846px">FOLLOW US ON</h5>
  <ul class="links"><li>Home</li><li>About Us</li><li>Services</li><li>Blog</li><li>Application</li><li>Donation</li><li>Contact Us</li></ul>
  <div class="contact">
    <div class="row"><svg width="12" height="16" viewBox="0 0 12 16"><path d="M6 0a6 6 0 0 0-6 6c0 4.5 6 10 6 10s6-5.5 6-10a6 6 0 0 0-6-6zm0 8.5A2.5 2.5 0 1 1 6 3.5a2.5 2.5 0 0 1 0 5z" fill="#e4222f"/></svg><span>Bully breed rescue<br>45215 Lorem ipsum dolor<br>sit amet, U.S.A</span></div>
    <div class="row"><svg width="14" height="14" viewBox="0 0 24 24"><path d="M6.6 10.8a15.1 15.1 0 0 0 6.6 6.6l2.2-2.2a1 1 0 0 1 1-.25 11.4 11.4 0 0 0 3.6.57 1 1 0 0 1 1 1V20a1 1 0 0 1-1 1A17 17 0 0 1 3 4a1 1 0 0 1 1-1h3.5a1 1 0 0 1 1 1c0 1.25.2 2.45.57 3.57a1 1 0 0 1-.25 1z" fill="#e4222f"/></svg><b>555-204-3187</b></div>
    <div class="row"><svg width="14" height="11" viewBox="0 0 14 11"><rect width="14" height="11" fill="#e4222f"/><path d="M0 0l7 6 7-6" stroke="#1a1616" fill="none"/></svg><span>hello@standuppup.org</span></div>
  </div>
  <div class="map" role="img" aria-label="Street map showing the rescue's location"></div>
  <div class="foot-brand"><span>Stand Up Pup</span></div>
  <div class="foot-socials"><i class="social"></i><i class="social"></i><i class="social"></i></div>
  <div class="copyright">© COPYRIGHT 2018 BULLY BREED RESCUE. ALL RIGHTS RESERVED.</div>
</footer>

</body>
</html>
```